Powerpoint template for Presenting Java Related Training

I am launching a website in 2017 called Kestrel Code Clinics that will offer training on advanced topics in Java programming. I need a Powerpoint template for use in the training courses. I have attached my logo. I am also attaching my business card design which was just completed ... I'd like to stay somewhat consistent between the different media, but without making the Powerpoint template too busy.
Updates

Project Deadline Extended Reason: Only 3 designs received and 2 days left so I am extending the deadline by 5 days. I would like to have at least 5 or 6 designs to consider before I make my decision. Added Sunday, October 30, 2016

Target Market(s)

Current and Prospective Software Developers

Industry/Entity Type

Software

Font styles to use
Serif
Sans Serif

Requirements
Must have
• Must use the provided logo and must use a color scheme that works well with the logo provided. Must be easy to read since this is for a training presentation and I don't want any distractions from the content.
Nice to have
• I would like to have alternatives for different types of content ... e.g. bullet lists vs. graphics, etc.
Should not have
• Just not too busy ... I want something that looks distinctive and nice but with minimal distractions.

```html
<!DOCTYPE html>
<html lang="en">
<head>
<meta charset="utf-8">
<title>Kestrel Code Clinics – Two Column Slide</title>
<link rel="stylesheet" href="https://fonts.googleapis.com/css2?family=Libre+Franklin:wght@400;500;600;700&family=Noto+Sans:wght@400&display=swap">
<style>
  :root {
    --brand-red: #cc2229;
    --brand-blue: #3169b0;
    --heading-blue: #1a6cb5;
    --text: #111111;
    --paper: #ffffff;
  }
  html, body {
    margin: 0;
    padding: 0;
    overflow: hidden;
    background: var(--paper);
  }
  .slide {
    position: relative;
    width: 1200px;
    height: 675px;
    overflow: hidden;
    background: var(--paper);
    font-family: "Noto Sans", Verdana, sans-serif;
    color: var(--text);
  }
  .header-banner {
    position: absolute;
    left: 0;
    top: 0;
    width: 1040px;
    height: 72px;
    background: linear-gradient(90deg, var(--brand-red) 0%, var(--brand-red) 40%, var(--brand-blue) 60%, var(--brand-blue) 100%);
  }
  .side-band {
    position: absolute;
    left: 1124px;
    top: 276px;
    width: 76px;
    height: 399px;
    background: var(--brand-blue);
  }
  .brand {
    position: absolute;
    left: 1040px;
    top: 40px;
    width: 130px;
    text-align: center;
    font-family: "Libre Franklin", Arial, sans-serif;
    font-weight: 700;
    font-size: 19px;
    line-height: 1.15;
    color: var(--brand-red);
  }
  .brand-dot {
    display: block;
    width: 22px;
    height: 22px;
    margin: 0 auto 8px;
    border-radius: 50%;
    background: var(--brand-blue);
  }
  .slide-title {
    position: absolute;
    left: 90px;
    top: 112px;
    margin: 0;
    font-family: "Libre Franklin", Arial, sans-serif;
    font-weight: 600;
    font-size: 49px;
    letter-spacing: -0.3px;
    color: var(--brand-red);
  }
  .column {
    position: absolute;
    top: 222px;
  }
  .column--one { left: 92px; }
  .column--two { left: 534px; }
  .category {
    margin: 0 0 26px;
    font-family: "Libre Franklin", Arial, sans-serif;
    font-weight: 500;
    font-size: 33px;
    letter-spacing: -0.6px;
    color: var(--heading-blue);
  }
  .column--two .bullets { margin-left: 39px; }
  .bullets {
    list-style: none;
    margin: 0;
    padding: 0;
  }
  .bullets li {
    position: relative;
    padding-left: 22px;
    white-space: nowrap;
  }
  .bullets li::before {
    content: "";
    position: absolute;
    left: 2px;
    top: 50%;
    width: 7px;
    height: 7px;
    margin-top: -4px;
    border-radius: 50%;
    background: var(--brand-red);
  }
  .level-1 { font-size: 30px; height: 41px; line-height: 41px; }
  .level-2 { font-size: 26px; height: 36px; line-height: 36px; margin-left: 45px; }
  .level-3 { font-size: 22px; height: 34px; line-height: 34px; margin-left: 90px; }
  .level-4 { font-size: 20px; height: 31px; line-height: 31px; margin-left: 135px; }
  .level-5 { font-size: 20px; height: 31px; line-height: 31px; margin-left: 180px; }
  .level-2::before, .level-3::before, .level-4::before, .level-5::before {
    width: 6px !important;
    height: 6px !important;
    margin-top: -3px !important;
  }
</style>
</head>
<body>
<main class="slide">
  <div class="header-banner" role="img" aria-label="Decorative header banner in brand red and blue"></div>
  <div class="side-band" aria-hidden="true"></div>

  <div class="brand">
    <span class="brand-dot"></span>
    Kestrel Code Clinics
  </div>

  <h1 class="slide-title">Slide title template</h1>

  <section class="column column--one">
    <h2 class="category">Category 1</h2>
    <ul class="bullets">
      <li class="level-1">Lorem Ipsum</li>
      <li class="level-2">Lorem Ipsum</li>
      <li class="level-3">Lorem Ipsum</li>
      <li class="level-4">Lorem Ipsum</li>
      <li class="level-5">Lorem Ipsum</li>
    </ul>
  </section>

  <section class="column column--two">
    <h2 class="category">Category 2</h2>
    <ul class="bullets">
      <li class="level-1">Lorem Ipsum</li>
      <li class="level-2">Lorem Ipsum</li>
      <li class="level-3">Lorem Ipsum</li>
      <li class="level-4">Lorem Ipsum</li>
      <li class="level-5">Lorem Ipsum</li>
    </ul>
  </section>
</main>
</body>
</html>
```